Penny auctions banner design to get people to sign up

Show the 3 steps needed to get started bidding with penny auctions on my website ZelNork.com. The core colors should be black, grey, and yellow.

It needs to show the following steps: 1) Register an account. 2) Purchase the starter package. 3) Start bidding and save up to 98% off!

Some creativity would be good so if you have some better ideas then please let them flow and show me your best banner design :) Thank you! Comment with any questions you have. Attached is my logo.

```html
<!DOCTYPE html>
<html lang="en">
<head>
<meta charset="utf-8">
<title>ZelNork – Penny Auction Banner Options</title>
<link rel="stylesheet" href="https://fonts.googleapis.com/css2?family=Fira+Sans+Condensed:wght@700;800&family=Lato:wght@400;700&family=Fjalla+One&display=swap">
<style>
  :root {
    --sheet-grey: #808080;
    --brand-yellow: #fcc324;
    --panel-dark: #3b3b3b;
    --panel-grey: #b4b4b4;
    --ink: #1c1c1c;
    --white: #ffffff;
    --frame-white: #ffffff;
    --frame-dark: #2f2f2f;
    --frame-light: #cfcfcf;
    --photo-deep: #4a3427;
    --photo-light: #e6e6e6;
  }
  html, body {
    margin: 0;
    padding: 0;
    width: 1200px;
    height: 1152px;
    overflow: hidden;
    background: var(--sheet-grey);
  }
  .sheet {
    position: relative;
    width: 1200px;
    height: 1152px;
  }
  .banner {
    position: absolute;
    display: block;
  }
  .banner--wide { left: 33px; width: 1135px; height: 153px; }
  .banner--compact { left: 33px; width: 631px; height: 153px; }

  .sample-label {
    position: absolute;
    left: 702px;
    margin: 0;
    font-family: "Fjalla One", "Arial Narrow", sans-serif;
    font-weight: 400;
    font-size: 48px;
    color: var(--white);
    transform: rotate(-7deg);
    transform-origin: left center;
    text-shadow: 1px 2px 3px rgba(0,0,0,0.35);
    letter-spacing: 0.5px;
  }

  .frame-white { fill: var(--frame-white); }
  .frame-dark { fill: var(--frame-dark); stroke: #4a4a4a; stroke-width: 2; stroke-dasharray: 3 3; }
  .frame-light { fill: var(--frame-light); stroke: #9a9a9a; stroke-width: 2; stroke-dasharray: 3 3; }

  .photo-backdrop { fill: var(--photo-light); }
  .yellow-block { fill: var(--brand-yellow); }
  .yellow-edge { fill: var(--white); }
  .steps-panel { fill: var(--panel-dark); }
  .logo-panel { fill: var(--panel-grey); }
  .divider-dark { fill: var(--ink); }

  .headline {
    font-family: "Fira Sans Condensed", "Arial Narrow", sans-serif;
    font-weight: 800;
    text-anchor: middle;
  }
  .headline--light { fill: var(--white); stroke: #3a3a3a; stroke-width: 1.4px; paint-order: stroke; }
  .headline--dark { fill: var(--ink); }

  .step-text {
    font-family: "Lato", Arial, sans-serif;
    font-weight: 400;
  }
  .step-text--light { fill: var(--white); }
  .step-text--dark { fill: var(--ink); }
  .step-badge--yellow { fill: var(--brand-yellow); }
  .step-badge--dark { fill: var(--ink); }
  .step-number {
    font-family: "Lato", Arial, sans-serif;
    font-weight: 700;
    text-anchor: middle;
  }
  .step-number--dark { fill: var(--ink); }
  .step-number--light { fill: var(--white); }

  .brand-mark { fill: var(--brand-yellow); stroke: var(--ink); stroke-width: 2; }
  .brand-name {
    font-family: "Fira Sans Condensed", "Arial Narrow", sans-serif;
    font-weight: 800;
    fill: var(--ink);
  }
  .cta-box { fill: var(--ink); }
  .cta-text {
    font-family: "Fira Sans Condensed", "Arial Narrow", sans-serif;
    font-weight: 700;
    fill: var(--white);
    text-anchor: middle;
  }
  .site-url {
    font-family: "Lato", Arial, sans-serif;
    font-weight: 700;
    fill: var(--ink);
    text-anchor: middle;
  }
</style>
</head>
<body>
<main class="sheet">

  <svg width="0" height="0" style="position:absolute" aria-hidden="true">
    <defs>
      <linearGradient id="photo-tones" x1="0" y1="0" x2="1" y2="0">
        <stop offset="0" stop-color="#4a3427"/>
        <stop offset="0.45" stop-color="#a89a86"/>
        <stop offset="1" stop-color="#e6e6e6"/>
      </linearGradient>

      <symbol id="banner-wide-content" viewBox="0 0 851 115">
        <rect class="photo-backdrop" x="4" y="4" width="250" height="107"/>
        <rect x="4" y="4" width="190" height="107" fill="url(#photo-tones)" role="img" aria-label="Photo of a smiling woman holding a fan of dollar bills"/>
        <polygon class="yellow-edge" points="172,4 442,4 410,111 172,111 200,57.5"/>
        <polygon class="yellow-block" points="180,7 434,7 404,108 180,108 207,57.5"/>
        <polygon class="steps-panel" points="440,4 712,4 676,111 408,111"/>
        <polygon class="logo-panel" points="712,4 847,4 847,111 676,111"/>

        <text class="headline headline--light" x="307" y="35" font-size="21">GET STARTED</text>
        <text class="headline headline--light" x="307" y="63" font-size="21">BIDDING WITH</text>
        <text class="headline headline--dark" x="307" y="94" font-size="25">PENNY AUCTIONS</text>

        <rect class="step-badge--yellow" x="440" y="25" width="12" height="12"/>
        <text class="step-number step-number--dark" x="446" y="35" font-size="11">1</text>
        <text class="step-text step-text--light" x="458" y="36" font-size="14">Register an account</text>
        <rect class="step-badge--yellow" x="440" y="45" width="12" height="12"/>
        <text class="step-number step-number--dark" x="446" y="55" font-size="11">2</text>
        <text class="step-text step-text--light" x="458" y="56" font-size="14">Purchase the starter package</text>
        <rect class="step-badge--yellow" x="440" y="65" width="12" height="12"/>
        <text class="step-number step-number--dark" x="446" y="75" font-size="11">3</text>
        <text class="step-text step-text--light" x="458" y="76" font-size="14">Start bidding and save up to</text>
        <text class="step-text step-text--light" x="458" y="94" font-size="14">98% off!</text>

        <rect class="brand-mark" x="682" y="50" width="30" height="30"/>
        <text class="brand-name" x="720" y="42" font-size="26">ZelNork</text>
        <rect class="cta-box" x="724" y="54" width="110" height="30"/>
        <text class="cta-text" x="779" y="76" font-size="19">LEARN MORE</text>
        <text class="site-url" x="760" y="104" font-size="12.5">http://ZelNork.com</text>
      </symbol>

      <symbol id="banner-compact-content" viewBox="0 0 473 115">
        <rect class="photo-backdrop" x="4" y="4" width="130" height="107"/>
        <rect x="4" y="4" width="100" height="107" fill="url(#photo-tones)" role="img" aria-label="Photo of a smiling woman holding a fan of dollar bills"/>
        <polygon class="yellow-edge" points="96,4 360,4 326,111 96,111 120,57.5"/>
        <polygon class="yellow-block" points="102,7 356,7 322,108 102,108 126,57.5"/>
        <polygon class="divider-dark" points="356,4 362,4 328,111 322,111"/>
        <polygon class="logo-panel" points="362,4 469,4 469,111 328,111"/>

        <text class="headline headline--light" x="234" y="25" font-size="16">GET STARTED BIDDING WITH</text>
        <text class="headline headline--dark" x="226" y="53" font-size="24">PENNY AUCTIONS</text>

        <rect class="step-badge--dark" x="120" y="64" width="11" height="11"/>
        <text class="step-number step-number--light" x="125.5" y="73" font-size="9.5">1</text>
        <text class="step-text step-text--dark" x="134" y="74" font-size="11.5">Register an account</text>
        <rect class="step-badge--dark" x="113" y="78" width="11" height="11"/>
        <text class="step-number step-number--light" x="118.5" y="87" font-size="9.5">2</text>
        <text class="step-text step-text--dark" x="128" y="88" font-size="11.5">Purchase the starter package</text>
        <rect class="step-badge--dark" x="106" y="92" width="11" height="11"/>
        <text class="step-number step-number--light" x="111.5" y="101" font-size="9.5">3</text>
        <text class="step-text step-text--dark" x="121" y="102" font-size="11.5">Start bidding and save up to 98% off!</text>

        <rect class="brand-mark" x="344" y="44" width="24" height="24"/>
        <text class="brand-name" x="372" y="34" font-size="21">ZelNork</text>
        <rect class="cta-box" x="378" y="44" width="86" height="28"/>
        <text class="cta-text" x="421" y="64" font-size="16">LEARN MORE</text>
        <text class="site-url" x="408" y="102" font-size="10.5">http://ZelNork.com</text>
      </symbol>
    </defs>
  </svg>

  <!-- Option 1: white frame -->
  <svg class="banner banner--wide" style="top:27px" viewBox="0 0 851 115" role="group" aria-label="Leaderboard banner, white frame">
    <rect class="frame-white" x="0" y="0" width="851" height="115"/>
    <use href="#banner-wide-content" x="0" y="0" width="851" height="115"/>
  </svg>
  <svg class="banner banner--compact" style="top:200px" viewBox="0 0 473 115" role="group" aria-label="Compact banner, white frame">
    <rect class="frame-white" x="0" y="0" width="473" height="115"/>
    <use href="#banner-compact-content" x="0" y="0" width="473" height="115"/>
  </svg>
  <p class="sample-label" style="top:222px">Sample 1</p>

  <!-- Option 2: dark frame -->
  <svg class="banner banner--wide" style="top:400px" viewBox="0 0 851 115" role="group" aria-label="Leaderboard banner, dark frame">
    <rect class="frame-dark" x="1" y="1" width="849" height="113"/>
    <use href="#banner-wide-content" x="0" y="0" width="851" height="115"/>
  </svg>
  <svg class="banner banner--compact" style="top:573px" viewBox="0 0 473 115" role="group" aria-label="Compact banner, dark frame">
    <rect class="frame-dark" x="1" y="1" width="471" height="113"/>
    <use href="#banner-compact-content" x="0" y="0" width="473" height="115"/>
  </svg>
  <p class="sample-label" style="top:596px">Sample 2</p>

  <!-- Option 3: light frame -->
  <svg class="banner banner--wide" style="top:787px" viewBox="0 0 851 115" role="group" aria-label="Leaderboard banner, light frame">
    <rect class="frame-light" x="1" y="1" width="849" height="113"/>
    <use href="#banner-wide-content" x="0" y="0" width="851" height="115"/>
  </svg>
  <svg class="banner banner--compact" style="top:960px" viewBox="0 0 473 115" role="group" aria-label="Compact banner, light frame">
    <rect class="frame-light" x="1" y="1" width="471" height="113"/>
    <use href="#banner-compact-content" x="0" y="0" width="473" height="115"/>
  </svg>
  <p class="sample-label" style="top:982px">Sample 3</p>

</main>
</body>
</html>
```